Business Card - Design

Create a business card design for my company with graphics on the front and a solid color on the back. The theme for the designs is going to be based on on chinese dragon festivals.

The back of the card will be the simplest as I only want a solid red color with my website address on it: www.bramblewickpies.com

For the front of the card I Want the following on the left side of the card:

Bramble Wick Hearth Pies
Lionel Ferris
(555) 284 - 7093
@bwhpriverbend

On the right side of the front of the card I want a dragon head either above or "eating" the abbreviation BWHP stacked two letters by two letters. I want all text and graphics to be red on the front of the card with the background being white.

The red used on the back and front of the card must match and be a deep red.
Examples of the red I am looking for, as well as some dragon heads, can be found at the links below:

http://pixelmorrow.example/forums/attachments/desktop-skins-toralind/4417d8830291546-desktop-skins-comet-saga-toralind-2.jpg

I like the overall head part of this picture, although the green would be replaced by red. I want a sharp dragon face and teeth/fangs, no whiskers, and no other body parts (arms, feet, etc.). Just the head eating the previously mentioned abbreviation.

```html
<!DOCTYPE html>
<html lang="en">
<head>
<meta charset="utf-8">
<title>Bramble Wick Hearth Pies – Business Card</title>
<link rel="stylesheet" href="https://fonts.googleapis.com/css2?family=Alegreya:wght@400;700&display=swap">
<style>
  :root {
    --deep-red: #85171c;
    --card-white: #ffffff;
    --backdrop: #e9e4de;
    --url-ink: #efe6e6;
  }
  * { margin: 0; padding: 0; box-sizing: border-box; }
  html, body {
    width: 1200px;
    height: 1200px;
    overflow: hidden;
    background: var(--backdrop);
    font-family: "Alegreya", Georgia, serif;
  }
  .sheet {
    position: relative;
    width: 1200px;
    height: 1200px;
  }
  .card {
    position: absolute;
    left: 150px;
    width: 900px;
    height: 514px;
    box-shadow: 0 6px 18px rgba(0,0,0,0.18);
  }
  .card-front {
    top: 66px;
    background: var(--card-white);
  }
  .card-back {
    top: 620px;
    background: var(--deep-red);
    display: flex;
    align-items: center;
    justify-content: center;
  }
  .divider {
    position: absolute;
    left: 0;
    right: 0;
    top: 246px;
    height: 6px;
    background: var(--deep-red);
  }
  .monogram {
    position: absolute;
    right: 60px;
    top: 92px;
    display: flex;
    align-items: center;
    gap: 24px;
  }
  .monogram-name {
    display: flex;
    flex-direction: column;
    font-weight: 700;
    font-size: 72px;
    line-height: 0.95;
    color: var(--deep-red);
    background: var(--card-white);
  }
  .monogram-mark {
    width: 130px;
    height: 130px;
    border-radius: 50%;
    background: var(--deep-red);
  }
  .contact {
    position: absolute;
    left: 52px;
    top: 278px;
    list-style: none;
    color: var(--deep-red);
    font-weight: 700;
    font-size: 30px;
    line-height: 42px;
  }
  .website {
    font-weight: 400;
    font-size: 44px;
    color: var(--url-ink);
    letter-spacing: 0.5px;
  }
</style>
</head>
<body>
<main class="sheet">
  <section class="card card-front" aria-label="Business card front">
    <div class="divider" aria-hidden="true"></div>
    <div class="monogram">
      <p class="monogram-name" aria-label="BWHP">
        <span>BW</span>
        <span>HP</span>
      </p>
      <span class="monogram-mark" aria-hidden="true"></span>
    </div>
    <ul class="contact">
      <li class="business">Bramble Wick Hearth Pies</li>
      <li class="person">Lionel Ferris</li>
      <li class="phone">(555) 284 - 7093</li>
      <li class="handle">@bwhpriverbend</li>
    </ul>
  </section>
  <section class="card card-back" aria-label="Business card back">
    <p class="website">www.bramblewickpies.com</p>
  </section>
</main>
</body>
</html>
```